Neuer Flyer für eine Therapeutin für Herzzentrierte Therapie...
Vielen Dank für die stets schnelle Bearbeitung und Rückantworten!
Zielgruppe
Herzenskommunikation ist meine Stärke, Menschen darin unterstützen ihre wahre Größe zu erkennen, meine Lebensaufgabe. Ich bin Therapeutin: Herzzentrierte Therapie, Lebensenergie Beratung, Bewegungsmeditation, Energetische Massagen. Meine Zielgruppe sind überwiegend Frauen, aber auch Männer mittleren Alters.
Aufgabenstellung
Bitte fließend und ohne Ecken und Kanten im Design. Text und Bilder liefere ich. Bzgl dem Format bin ich eher traditionell.
Mühlenhof Logo / Foto Sabine Lorenz
Herzenskommunikation ist meine Stärke, Menschen darin unterstützen ihre wahre Größe zu erkennen, meine Lebensaufgabe
Herzzentrierte Therapie
Lebensenergie Beratung
Bewegungsmeditation
Energie-Massagen
Call to action button Vereinbare jetzt einen Termin unter +49 (0)157-36470918
Sabine Lorenz
Birkenfeld-Auerweg 8 I 93087 Tessenried
kontakt@muehlenhofamweiher.de I www.muehlenhofamweiher.de/sabine
 Du möchtest sinnerfüllter leben und dich freier fühlen?
 Ins Gleichgewicht und gesund auf allen Ebenen - mental, emotional und körperlich - sein?
 Du möchtest Beziehungen leben, die auf Liebe, Vertrauen, Respekt und Authentizität basieren?
 Bedingungslos glücklich, zentriert, bewusst, erfolgreich und im Frieden mit Dir sein?
 Du möchtest Dein Wohlbefinden steigern?
… Dann bist du hier genau richtig!
Herzzentrierte Therapie ist ein liebevoller Ansatz zur emotionalen und spirituellen Heilung, bei der Du Dich der Weisheit Deines Herzens anvertraust. Ich unterstütze Dich, in Dialog mit Deinem Herzen zu gehen und Deine eigene innere Weisheit wahrzunehmen - dieser zu vertrauen, alte Glaubenssätze zu beleuchten und neu zu fassen oder ungelöste Emotionen aufzudecken, zu transformieren und zu reintegrieren. Dauer beim Ersttermin ca. 90 Minuten, bei Folgeterminen ca. 60 Minuten
Da wo Dein Herz ist, Da ist auch Dein Schatz!
Dieser konzentrativ-meditative Bewegungsablauf mit QiGong-Bewegungen in Kombination mit positiven Affirmationen wird im Stand ausgeführt; es ist bei Bedarf auch eine Ausführung davon im Sitzen möglich. Die Bewegungsmeditation ermöglicht Dir Deine Körperwahrnehmung zu schärfen und Einzutauchen in Gegenwärtigkeit des Seins. Die A..

```html
<!DOCTYPE html>
<html lang="de">
<head>
<meta charset="utf-8">
<title>Flyer Sabine Lorenz – Herzzentrierte Therapie</title>
<link href="https://fonts.googleapis.com/css2?family=Dancing+Script:wght@500;700&family=Figtree:wght@400;600;700&display=swap" rel="stylesheet">
<style>
  :root{
    --paper:#ffffff;
    --panel-soft:#f5f4f2;
    --ink:#1a1a1a;
    --black:#000000;
    --taupe:#b0a48a;
    --photo-dark:#2b1d14;
    --photo-mid:#5a3b25;
    --white:#ffffff;
  }
  *{margin:0;padding:0;box-sizing:border-box}
  html,body{width:1200px;height:1200px;overflow:hidden;background:var(--paper)}
  body{font-family:"Figtree",Arial,sans-serif;color:var(--ink);position:relative}
  .script{font-family:"Dancing Script",cursive}

  .flyer{position:absolute;left:78px;top:229px;width:1051px;height:749px;display:flex;
    box-shadow:0 4px 14px rgba(0,0,0,.12)}
  .panel{position:relative;height:100%;overflow:hidden}
  .panel--voucher{width:346px;background:var(--paper)}
  .panel--about{width:352px;background:var(--panel-soft)}
  .panel--cover{width:353px;background:var(--paper)}

  /* left panel */
  .voucher-title{position:absolute;left:34px;top:36px;font-size:32px;font-weight:500;color:var(--taupe)}
  .voucher-text{position:absolute;left:36px;top:89px;width:282px;font-size:12.8px;line-height:17.5px}
  .info-band{position:absolute;left:0;top:230px;width:346px;height:114px;background:var(--black);
    color:var(--white);padding:17px 6px 0 36px;font-size:12.5px;font-weight:600;line-height:17.5px}
  .info-band p+p{margin-top:7px}
  .info-band .nowrap{white-space:nowrap;font-size:11.6px}
  .brand-small{position:absolute;left:36px;top:550px;width:110px;text-align:center;
    font-size:15px;font-weight:600;line-height:18px;color:var(--ink)}
  .contact{position:absolute;left:36px;top:624px;font-size:10.6px;line-height:15.6px;font-style:normal}
  .contact strong{font-weight:700}

  /* middle panel */
  .about-kicker{position:absolute;left:34px;top:36px;font-size:29px;font-weight:700;line-height:36px}
  .about-title{position:absolute;left:34px;top:80px;width:300px;font-size:33px;font-weight:700;line-height:40px}
  .about-text{position:absolute;left:36px;top:190px;width:280px;font-size:12.8px;line-height:17.5px}
  .about-text p+p{margin-top:17.5px}
  .about-text .closing{font-weight:700}

  /* right panel */
  .portrait{position:absolute;left:0;top:0;width:353px;height:520px;
    background:linear-gradient(180deg,var(--photo-dark) 0%,var(--photo-mid) 30%,#7a5a40 55%,#b7a796 75%,rgba(255,255,255,0) 100%)}
  .cover-quote{position:absolute;left:48px;top:34px;width:257px;text-align:center;color:var(--white);
    font-size:23px;font-weight:500;line-height:27.5px}
  .cta-badge{position:absolute;left:20px;top:204px;width:95px;height:95px;border-radius:50%;
    background:var(--white);display:flex;flex-direction:column;align-items:center;justify-content:center;
    text-align:center;font-size:8px;line-height:11px;padding:0 9px}
  .cta-badge strong{font-weight:700}
  .brand-large{position:absolute;left:0;width:353px;top:490px;text-align:center;
    font-size:26px;font-weight:600;line-height:30px;color:var(--ink)}
  .services{position:absolute;left:0;width:353px;top:610px;text-align:center;list-style:none;
    color:var(--taupe);font-size:15px;font-weight:700;line-height:20.3px}
  .cover-web{position:absolute;left:0;width:353px;top:700px;text-align:center;font-size:11px;font-weight:600}
</style>
</head>
<body>
<main class="flyer">
  <section class="panel panel--voucher">
    <h2 class="voucher-title script">Gutschein</h2>
    <p class="voucher-text">Schenke deinem Herzensmenschen das Gefühl WICHTIG zu sein! Einen Gutschein für eines meiner Angebote kann ich dir jederzeit gerne in Printform oder auch online per Mail zukommen lassen oder du kannst diesen direkt bei uns im Hofladen erwerben.</p>
    <div class="info-band">
      <p>Informiere Dich jetzt über mein Angebot<br>unter 0157-36470918</p>
      <p>Termine nach persönlicher Absprache,<br><span class="nowrap">Preise siehe unter www.muehlenhofamweiher.de/sabine</span></p>
    </div>
    <div class="brand-small">Mühlenhof<br>am Weiher</div>
    <address class="contact">
      <strong>Sabine Lorenz</strong><br>
      Birkenfeld-Auerweg 8<br>
      93087 Tessenried<br>
      +49 (0)157-36470918<br>
      kontakt@muehlenhofamweiher.de/sabine<br>
      www.muehlenhofamweiher.de
    </address>
  </section>

  <section class="panel panel--about">
    <h2 class="about-kicker script">Wer ich bin…</h2>
    <h1 class="about-title script">Herzenskommunikation<br>ist meine Stärke!</h1>
    <div class="about-text">
      <p>Zahlreiche therapeutische und persönliche Weiterbildungen in Verbindung mit meiner Grundausbildung als Sport- und Physiotherapeutin, meiner Lebenserfahrung sowie meiner intuitiven Kraft und Empathie ermöglichen es mir, Menschen tief im Herzen wahrzunehmen und zu berühren. Ich fühle mich gesegnet, das Wirken der „inneren Weisheit“ im Menschen während der Behandlungen miterleben zu dürfen. Gaben sehe ich vor allem in der Aktivierung der Selbstheilungskräfte und der Bewusstseinsentwicklung. Allen Menschen haben es verdient, sich in ihrer wahren Größe wahrzunehmen und ihr ureigenes Potenzial zu entfalten.</p>
      <p>Das Wunder Leben hat mich zu der Frau heranreifen lassen, die ich heute bin. Meine Nahtoderfahrung nach einem Unfall hat mein Bewusstseinstor geöffnet und mich zudem darin bestärkt, mich vollkommen, mit all meinen Gaben und Talenten in diese Welt einzubringen. Ich bin eine offene Frau, die Zuhause angekommen ist - ihre Kraft, Liebe und tiefen inneren Frieden gefunden hat.</p>
      <p class="closing">… aus diesem Grund bin ich Anlaufstelle für Herzensmenschen jeden Alters, die ihre Lebensenergie auf das nächste Level anheben wollen!</p>
    </div>
  </section>

  <section class="panel panel--cover">
    <div class="portrait" role="img" aria-label="Porträtfoto von Sabine Lorenz, lächelnd in weißer Bluse vor einer alten Holztür"></div>
    <p class="cover-quote script">Herzenskommunikation ist meine Stärke, Menschen darin unterstützen ihre wahre Größe zu erkennen, meine Lebensaufgabe.</p>
    <div class="cta-badge"><strong>Sabine<br>Lorenz:</strong>Vereinbare jetzt einen Termin unter +49 (0)157-36470918</div>
    <div class="brand-large">Mühlenhof<br>am Weiher</div>
    <ul class="services">
      <li>Herzzentrierte Therapie</li>
      <li>Lebensenergie Beratung</li>
      <li>Bewegungsmeditation</li>
      <li>Energie-Massagen</li>
    </ul>
    <p class="cover-web">www.muehlenhofamweiher.de</p>
  </section>
</main>
</body>
</html>
```